Homepage Redesign for Healthcare Tech Company

This is for a redesign of our current homepage. We have specific notes and a Mockup and we need a great designer to bring it to life and make it look sophisticated and professional. Please see the Current Page (attached and online) as well as the Notes doc and Mockup PPT, both attached, for what we need.

Overall, look at the current page as a sketch of what it could be. We would like a design that really nails the structure of both the overall page and the pipeline (that runs through Sections 1-4), so that it looks like one, clean, custom design (not pieced together). It’s important that the basic structure of the pipeline, especially the transition from icons to screenshots (starting in section 2, and mostly in section 3) all flow together well and look like a deliberate, well thought-out design. Please include that, and at least the headlines for each section, in any initial submissions.

We will be building out of website beyond just this page, and would be great to work with a designer we can continue working with on the website, the graphical screenshots and some infographics. Not a must but definitely an option if you would like. We didn’t include all pages in this project, because we would like the designer to focus all energy on creating a well thought-out homepage design with the wow factor, and we can build it out together from there. For now, we would like just 2 additional general theme pages (one smaller page for a couple paragraphs of text only and one with a few uniform sections, with room for text and small graphic-see notes).

Our customers are healthcare companies – both Doctors and IT professionals of medium to large healthcare organizations who support doctors. We are experts in healthcare interoperability technology and the page should reflect that. Medical Record documentation is an expensive time-consuming massive headache for our customer base. What we are offering is a truly groundbreaking solution that leverages the best technology available to bring them something that wasn’t possible before – ALL of their patient data in one enriched and linked document, delivered to their current workflow. It's an expensive solution but very impactful in terms of better patient care and dramatically streamlined workflow - the homepage needs to reflect that. Please take the time to understand the solution we offer and just let me know if you need clarification – I’m happy to answer any questions.

Thanks!

SEE ATTACHMENTS, and also this more detailed breakdown of the sections: https://qv.fx/Tr4mPz

Target Market(s)

Doctors, IT Professionals in the Healthcare field, Medical Coders..but focus should be on Doctors

Number of Pages Required

1 page

Colors
0355a3
3276b5
0293ce
6b449b
886aae
b7a5cd
00a990
33b8a4
86cfc6

Requirements
Must have
• - Sophisticated, professional, masterful layout
- Must refer to the attached DESIGN NOTES.doc (about 2 pages) and MOCKUP.PPT but bring the idea to life in an innovative way. In general, we collect all medical records, summarize and unify into 1 document that we send straight into each patient file, but referring to the actual notes to truly get what we do and what we need it is a must.
- Framing/background emphasis for provided screenshots (even if these screenshots don't fit exactly, we will make them fit after)
- Emphasis on the fact that clicking the View Source buttons in the Lumora (what we call our product) opens the actual source documents (underlying medical record) - this is a big deal for doctors and medical coders.
- Final design should be in editable PSD file
Nice to have
• Animation. We are asking for design only because we want the best design possible but we would definitely choose a great animated design (assuming that means you'd need to code it too - let me know) and ensure that you are paid the extra for coding if you need to code it yourself.
Should not have
• template feel - should look custom
cheesy photos of models dressed as doctors

```html
<!DOCTYPE html>
<html lang="en">
<head>
<meta charset="utf-8">
<title>Clarivio – Unified Patient Intelligence</title>
<link href="https://fonts.googleapis.com/css2?family=Sora:wght@300;400;500;600;700&display=swap" rel="stylesheet">
<style>
:root{
  --ink:#0b0b10;
  --ink-2:#14141c;
  --ink-3:#1d1d27;
  --line-dark:#2b2b38;
  --white:#ffffff;
  --text:#22242c;
  --muted:#6c6f7c;
  --muted-dark:#9a9cab;
  --blue:#0355a3;
  --blue-2:#3276b5;
  --cyan:#0293ce;
  --purple:#6b449b;
  --purple-2:#886aae;
  --lilac:#b7a5cd;
  --teal:#00a990;
  --teal-2:#33b8a4;
  --mint:#86cfc6;
}
*{margin:0;padding:0;box-sizing:border-box}
html,body{width:1200px;height:4152px;overflow:hidden}
body{font-family:"Sora",Arial,sans-serif;color:var(--text);background:var(--ink);position:relative}
.abs{position:absolute}
.btn{display:inline-block;font-size:10px;font-weight:600;letter-spacing:.08em;text-transform:uppercase;color:#fff;padding:9px 18px;border-radius:3px;text-decoration:none}
.btn--teal{background:var(--teal)}
.btn--purple{background:var(--purple)}

/* nav */
.nav{position:absolute;left:0;top:0;width:1200px;height:60px;display:flex;align-items:center;padding:0 40px;z-index:3}
.nav__links{display:flex;gap:28px;font-size:12px;color:#d9d9e3;flex:1}
.nav__right{display:flex;gap:28px;align-items:center;font-size:12px;color:#d9d9e3;flex:1;justify-content:flex-end}
.brand{display:flex;align-items:center;gap:10px;color:#fff;font-weight:600;font-size:20px;letter-spacing:.04em}
.brand__dot{width:20px;height:20px;border-radius:4px;background:var(--cyan)}

/* hero */
.hero{position:absolute;left:0;top:0;width:1200px;height:600px;background:var(--ink);overflow:hidden}
.hero__photo{position:absolute;right:0;top:0;width:760px;height:600px;background:linear-gradient(90deg,var(--ink) 0%,rgba(11,11,16,.6) 35%,rgba(60,58,70,.55) 100%),linear-gradient(160deg,#4a4853,#2a2930 60%,#1a1a20)}
.hero__content{position:absolute;left:60px;top:340px;width:520px}
.hero h1{color:#fff;font-size:34px;font-weight:600;margin-bottom:12px}
.hero__lead{color:#fff;font-size:15px;line-height:1.45;font-weight:500;margin-bottom:16px}
.hero__body{color:var(--muted-dark);font-size:10px;line-height:1.6;margin-bottom:22px}

/* network */
.network{position:absolute;left:0;top:600px;width:1200px;height:640px;background:var(--ink)}
.section-title{text-align:center;font-size:24px;font-weight:600}
.section-sub{text-align:center;font-size:13px;line-height:1.5;margin-top:10px}
.network .section-title,.network .section-sub{color:#fff}
.network__label{text-align:center;color:#fff;font-size:18px;font-weight:600;margin-top:14px}
.network__hub{position:absolute;left:500px;top:160px;width:200px;height:360px;border-radius:50%;background:radial-gradient(circle at 50% 55%,rgba(2,147,206,.55) 0%,rgba(107,68,155,.25) 45%,rgba(11,11,16,0) 72%)}
.node{position:absolute;width:240px}
.node h3{color:#fff;font-size:13px;font-weight:600;margin-bottom:8px}
.node p{color:var(--muted-dark);font-size:9px;line-height:1.6}
.node-icon{position:absolute;width:44px;height:44px;border-radius:8px;border:1.5px solid var(--purple-2);display:flex;align-items:center;justify-content:center;background:var(--ink-2)}

/* light sections */
.light{position:absolute;left:0;width:1200px;background:var(--white)}
.feature-title{font-size:26px;font-weight:600;line-height:1.25;color:var(--text);margin-bottom:18px}
.feature-body{font-size:10px;line-height:1.7;color:var(--muted);margin-bottom:12px}
.feature-sub{font-size:13px;font-weight:600;color:var(--text);margin:14px 0 6px}

.shot{position:absolute;background:#fff;border:1px solid #dfe1e8;border-radius:6px;box-shadow:0 14px 40px rgba(20,20,40,.16);overflow:hidden;padding:14px 16px}
.shot__bar{display:flex;align-items:center;gap:8px;font-size:11px;font-weight:600;color:var(--blue);padding-bottom:10px;border-bottom:2px solid var(--blue);margin-bottom:10px}
.shot__bar i{width:12px;height:12px;border-radius:2px;background:var(--blue)}
.shot__h{font-size:10px;font-weight:600;color:var(--text);margin:10px 0 6px}
.row{display:flex;gap:8px;margin-bottom:5px}
.row span{height:7px;border-radius:2px;background:#e6e8ee}
.row span.k{background:#c9d6ea}
.pill{height:8px;width:26px;border-radius:4px;display:inline-block}

.logos{position:absolute;left:0;top:2460px;width:1200px;height:80px;display:flex;background:#f1f2f5}
.logos div{flex:1;display:flex;align-items:center;justify-content:center;font-size:14px;font-weight:600;color:#3a3c46;border-right:1px solid #e1e3e9}
.logos div.on{background:#fff}

/* dark footer area */
.benefits{position:absolute;left:0;top:2990px;width:1200px;height:300px;background:var(--ink)}
.benefit{position:absolute;top:40px;width:200px;text-align:center}
.benefit h4{color:#fff;font-size:13px;font-weight:600;margin:18px 0 8px}
.benefit p{color:var(--muted-dark);font-size:9px;line-height:1.6}
.blog{position:absolute;left:0;top:3290px;width:1200px;height:500px;background:var(--ink)}
.blog .section-title{color:#fff}
.card{position:absolute;top:80px;width:300px}
.card__img{height:170px;background:linear-gradient(160deg,#5e5d68,#2c2b33)}
.card__box{background:#fff;width:200px;margin:-50px auto 0;position:relative;padding:18px 16px;font-size:12px;font-weight:600;line-height:1.45;color:var(--text)}
.card .btn{display:block;width:110px;margin:16px auto 0;text-align:center}
.footer{position:absolute;left:0;top:3790px;width:1200px;height:362px;background:#08080c;padding:36px 60px}
.footer p{color:var(--muted-dark);font-size:9px;line-height:1.7;margin-bottom:10px;max-width:1080px}
.footer__rule{border-top:1px solid var(--line-dark);margin:22px 0 14px}
.footer__copy{color:#6b6d7a;font-size:8px}
</style>
</head>
<body>

<header class="nav">
  <nav class="nav__links"><span>About Us</span><span>Features</span><span>Process</span></nav>
  <div class="brand"><span class="brand__dot"></span>CLARIVIO</div>
  <div class="nav__right"><span>Team</span><span>Clients</span><a class="btn btn--teal">Request Demo</a></div>
</header>

<section class="hero">
  <div class="hero__photo" role="img" aria-label="Clinician reviewing patient records in a dimly lit hospital corridor"></div>
  <div class="hero__content">
    <h1>Unified Patient Intelligence</h1>
    <p class="hero__lead">Each patients' full medical history, summary and analysis in one comprehensive health record</p>
    <p class="hero__body">Clarivio collects patients' records from all sources of external clinical data, synthesizes the captured data into one complete health record, distills all HCC, MIPS and HEDIS opportunities, and delivers them directly into your EHR, all in a matter of hours.</p>
    <a class="btn btn--purple">Request Demo</a>
  </div>
</section>

<section class="network">
  <h2 class="section-title" style="padding-top:30px">Your Patients' Full Medical History From All Sources</h2>
  <p class="section-sub">Each patients' full medical history, summary and analysis in one<br>comprehensive health record</p>
  <p class="network__label">Clarivio Clinical Data Network</p>

  <div class="network__hub" role="img" aria-label="Illustration of the clinical data network hub linking all six data sources"></div>

  <div class="node-icon" style="left:430px;top:168px"><svg width="22" height="22" viewBox="0 0 22 22" fill="none" stroke="#b7a5cd" stroke-width="1.5"><rect x="3" y="4" width="16" height="12" rx="1"/><path d="M8 19h6"/></svg></div>
  <div class="node-icon" style="left:430px;top:310px"><svg width="22" height="22" viewBox="0 0 22 22" fill="none" stroke="#b7a5cd" stroke-width="1.5"><rect x="6" y="3" width="10" height="16" rx="2"/><path d="M6 9h10"/></svg></div>
  <div class="node-icon" style="left:430px;top:452px"><svg width="22" height="22" viewBox="0 0 22 22" fill="none" stroke="#b7a5cd" stroke-width="1.5"><path d="M9 3v6l-5 9h14l-5-9V3"/><path d="M8 3h6"/></svg></div>
  <div class="node-icon" style="left:726px;top:168px"><svg width="22" height="22" viewBox="0 0 22 22" fill="none" stroke="#b7a5cd" stroke-width="1.5"><rect x="4" y="8" width="14" height="9" rx="1"/><path d="M7 8V3h8v5"/></svg></div>
  <div class="node-icon" style="left:726px;top:310px"><svg width="22" height="22" viewBox="0 0 22 22" fill="none" stroke="#b7a5cd" stroke-width="1.5"><circle cx="11" cy="11" r="3"/><circle cx="4" cy="5" r="2"/><circle cx="18" cy="5" r="2"/><circle cx="11" cy="19" r="2"/><path d="M6 6l3 3M16 6l-3 3M11 14v3"/></svg></div>
  <div class="node-icon" style="left:726px;top:452px"><svg width="22" height="22" viewBox="0 0 22 22" fill="none" stroke="#b7a5cd" stroke-width="1.5"><ellipse cx="11" cy="5" rx="7" ry="2.5"/><path d="M4 5v12c0 1.4 3 2.5 7 2.5s7-1.1 7-2.5V5M4 11c0 1.4 3 2.5 7 2.5s7-1.1 7-2.5"/></svg></div>

  <div class="node" style="left:160px;top:172px"><h3>EMR Networks</h3><p>Connected to 400,000 physician EHR endpoints and over 40,000 facilities across the country.</p></div>
  <div class="node" style="left:160px;top:314px"><h3>RX Data or US Pharmacies</h3><p>Comprehensive medication history including prescribed doses, adherence and refill patterns through the Rxlink pharmacy data network.</p></div>
  <div class="node" style="left:160px;top:456px"><h3>Diagnostic Labs</h3><p>Clarivio is directly connected to all major diagnostic testing laboratories, enabling collection of all lab results.</p></div>
  <div class="node" style="left:800px;top:172px"><h3>Provider Faxes</h3><p>Our records received from PCPs and specialists are converted into structured, searchable electronic records in C-CDA for ingestion.</p></div>
  <div class="node" style="left:800px;top:314px"><h3>HIE Networks</h3><p>Aggregating from 50 Health Information Exchange networks for seamless access to clinical data.</p></div>
  <div class="node" style="left:800px;top:456px"><h3>Claims Databases</h3><p>Claims data is the richest longitudinal source for past visits and medications, including Medicare Part A, B and D data for all Medicare beneficiaries.</p></div>
</section>

<section class="light" style="top:1240px;height:600px">
  <div class="abs" style="left:60px;top:130px;width:500px">
    <h2 class="feature-title">Transformed Into 1 Composite C-Cda<br>Health Record</h2>
    <p class="feature-body">The Clarivio data synthesis engine utilizes HL7 FHIR, advanced parsing technologies, Clinical Natural Language Processing (cNLP), proprietary logic and ML modeling to clean, de-duplicate, structure and enrich all inputs from data acquisition.</p>
    <p class="feature-body">The normalized data is unified into the Clarivio Lumora C-CDA, an enhanced composite longitudinal record in C-CDA format, the industry standard for all interoperability initiatives.</p>
  </div>
  <div class="shot" style="left:660px;top:120px;width:440px;height:380px">
    <div class="shot__bar"><i></i>CLARIVIO</div>
    <div class="shot__h">Insurance Providers</div>
    <div class="row"><span class="k" style="width:90px"></span><span style="width:110px"></span><span style="width:80px"></span><span style="width:90px"></span></div>
    <div class="row"><span style="width:90px"></span><span style="width:110px"></span><span style="width:80px"></span><span style="width:90px"></span></div>
    <div class="shot__h">Medications</div>
    <div class="row"><span class="k" style="width:120px"></span><span style="width:70px"></span><span style="width:80px"></span><span style="width:100px"></span></div>
    <div class="row"><span style="width:120px"></span><span style="width:70px"></span><span style="width:80px"></span><span style="width:100px"></span></div>
    <div class="row"><span style="width:120px"></span><span style="width:70px"></span><span style="width:80px"></span><span style="width:100px"></span></div>
    <div class="row"><span style="width:120px"></span><span style="width:70px"></span><span style="width:80px"></span><span style="width:100px"></span></div>
    <div class="shot__h">Results</div>
    <div class="row"><span class="k" style="width:100px"></span><span style="width:130px"></span><span style="width:140px"></span></div>
    <div class="row"><span style="width:100px"></span><span style="width:130px"></span><span style="width:140px"></span></div>
    <div class="shot__h">Problems</div>
    <div class="row"><span class="k" style="width:150px"></span><span style="width:90px"></span><span style="width:130px"></span></div>
    <div class="row"><span style="width:150px"></span><span style="width:90px"></span><span style="width:130px"></span></div>
  </div>
</section>

<section class="light" style="top:1840px;height:440px">
  <div class="shot" style="left:100px;top:20px;width:430px;height:380px">
    <div class="shot__bar"><i></i>CLARIVIO <span style="margin-left:auto;font-size:9px;color:var(--muted);font-weight:500">Lumora Summary</span></div>
    <div class="row"><span class="k" style="width:150px"></span><span class="k" style="width:60px"></span><span class="k" style="width:60px"></span><span class="k" style="width:60px"></span></div>
    <div style="display:flex;flex-direction:column;gap:9px;margin-top:10px">
      <div class="row"><span style="width:150px"></span><i class="pill" style="background:var(--teal)"></i><span style="width:40px"></span><i class="pill" style="background:var(--cyan)"></i><span style="width:60px"></span></div>
      <div class="row"><span style="width:150px"></span><i class="pill" style="background:var(--teal)"></i><span style="width:40px"></span><i class="pill" style="background:var(--cyan)"></i><span style="width:60px"></span></div>
      <div class="row"><span style="width:150px"></span><i class="pill" style="background:var(--purple-2)"></i><span style="width:40px"></span><i class="pill" style="background:var(--cyan)"></i><span style="width:60px"></span></div>
      <div class="row"><span style="width:150px"></span><i class="pill" style="background:var(--teal)"></i><span style="width:40px"></span><i class="pill" style="background:var(--cyan)"></i><span style="width:60px"></span></div>
      <div class="row"><span style="width:150px"></span><i class="pill" style="background:var(--teal)"></i><span style="width:40px"></span><i class="pill" style="background:var(--lilac)"></i><span style="width:60px"></span></div>
      <div class="row"><span style="width:150px"></span><i class="pill" style="background:var(--teal)"></i><span style="width:40px"></span><i class="pill" style="background:var(--cyan)"></i><span style="width:60px"></span></div>
      <div class="row"><span style="width:150px"></span><i class="pill" style="background:var(--purple-2)"></i><span style="width:40px"></span><i class="pill" style="background:var(--cyan)"></i><span style="width:60px"></span></div>
      <div class="row"><span style="width:150px"></span><i class="pill" style="background:var(--teal)"></i><span style="width:40px"></span><i class="pill" style="background:var(--cyan)"></i><span style="width:60px"></span></div>
      <div class="row"><span style="width:150px"></span><i class="pill" style="background:var(--teal)"></i><span style="width:40px"></span><i class="pill" style="background:var(--cyan)"></i><span style="width:60px"></span></div>
      <div class="row"><span style="width:150px"></span><i class="pill" style="background:var(--teal)"></i><span style="width:40px"></span><i class="pill" style="background:var(--lilac)"></i><span style="width:60px"></span></div>
      <div class="row"><span style="width:150px"></span><i class="pill" style="background:var(--teal)"></i><span style="width:40px"></span><i class="pill" style="background:var(--cyan)"></i><span style="width:60px"></span></div>
      <div class="row"><span style="width:150px"></span><i class="pill" style="background:var(--purple-2)"></i><span style="width:40px"></span><i class="pill" style="background:var(--cyan)"></i><span style="width:60px"></span></div>
      <div class="row"><span style="width:150px"></span><i class="pill" style="background:var(--teal)"></i><span style="width:40px"></span><i class="pill" style="background:var(--cyan)"></i><span style="width:60px"></span></div>
    </div>
  </div>
  <div class="abs" style="left:640px;top:30px;width:470px">
    <h2 class="feature-title">Summarized And Linked to<br>Key Insights</h2>
    <p class="feature-body">Insights are presented in a succinct summary with direct links to supporting evidence. HCC, HEDIS and MIPS opportunities are abstracted and cross-linked directly to the original text in the underlying record for quick and easy reference.</p>
    <h3 class="feature-sub">Risk Adjustment</h3>
    <p class="feature-body">HCC opportunities for new capture and recapture are identified and extracted using logic algorithms.</p>
    <h3 class="feature-sub">Quality Analysis</h3>
    <p class="feature-body">HEDIS and MIPS quality measure gaps closed using NCQA certified technology to generate QRDAs.</p>
  </div>
</section>

<section class="light" style="top:2280px;height:710px">
  <h2 class="section-title" style="padding-top:20px">Delivered Directly into Your EHR for Native Viewing</h2>
  <p class="section-sub" style="color:var(--muted);font-size:11px">The final package is delivered as a single longitudinal record into each patient's chart within your EHR, viewable natively.<br>The Clarivio Lumora is compatible with any Meaningful Use certified EHR.</p>
</section>
<div class="logos">
  <div>Nordwell</div><div>CarePath</div><div>Helixa</div><div class="on">Orbisa</div><div>Meridia</div><div>Fernhill</div><div>Solvent</div><div>Quillon</div>
</div>
<div class="shot" style="left:340px;top:2600px;width:520px;height:340px;z-index:1">
  <div class="shot__bar"><i></i>CLARIVIO</div>
  <div class="row"><span class="k" style="width:140px"></span><span class="k" style="width:90px"></span><span class="k" style="width:90px"></span><span class="k" style="width:120px"></span></div>
  <div style="display:flex;flex-direction:column;gap:8px;margin-top:12px">
    <div class="row"><span style="width:140px"></span><span style="width:90px"></span><span style="width:90px"></span><span style="width:120px"></span></div>
    <div class="row"><span style="width:140px"></span><span style="width:90px"></span><span style="width:90px"></span><span style="width:120px"></span></div>
    <div class="row"><span style="width:140px"></span><span style="width:90px"></span><span style="width:90px"></span><span style="width:120px"></span></div>
    <div class="row"><span style="width:140px"></span><span style="width:90px"></span><span style="width:90px"></span><span style="width:120px"></span></div>
    <div class="row"><span style="width:140px"></span><span style="width:90px"></span><span style="width:90px"></span><span style="width:120px"></span></div>
    <div class="row"><span style="width:140px"></span><span style="width:90px"></span><span style="width:90px"></span><span style="width:120px"></span></div>
    <div class="row"><span style="width:140px"></span><span style="width:90px"></span><span style="width:90px"></span><span style="width:120px"></span></div>
    <div class="row"><span style="width:140px"></span><span style="width:90px"></span><span style="width:90px"></span><span style="width:120px"></span></div>
    <div class="row"><span style="width:140px"></span><span style="width:90px"></span><span style="width:90px"></span><span style="width:120px"></span></div>
    <div class="row"><span style="width:140px"></span><span style="width:90px"></span><span style="width:90px"></span><span style="width:120px"></span></div>
    <div class="row"><span style="width:140px"></span><span style="width:90px"></span><span style="width:90px"></span><span style="width:120px"></span></div>
    <div class="row"><span style="width:140px"></span><span style="width:90px"></span><span style="width:90px"></span><span style="width:120px"></span></div>
    <div class="row"><span style="width:140px"></span><span style="width:90px"></span><span style="width:90px"></span><span style="width:120px"></span></div>
    <div class="row"><span style="width:140px"></span><span style="width:90px"></span><span style="width:90px"></span><span style="width:120px"></span></div>
  </div>
</div>

<section class="benefits">
  <div class="benefit" style="left:120px">
    <svg width="80" height="80" viewBox="0 0 80 80" fill="none"><circle cx="40" cy="40" r="36" stroke="#2b2b38" stroke-width="3"/><path d="M40 4a36 36 0 0 1 34 26" stroke="#00a990" stroke-width="3"/><path d="M34 28l16 12-8 2 4 9-4 2-4-9-6 5z" fill="#33b8a4"/></svg>
    <h4>Click Access</h4><p>Click access to each reference and insight in the underlying record.</p>
  </div>
  <div class="benefit" style="left:380px">
    <svg width="80" height="80" viewBox="0 0 80 80" fill="none"><circle cx="40" cy="40" r="36" stroke="#2b2b38" stroke-width="3"/><path d="M76 40a36 36 0 0 1-30 35" stroke="#00a990" stroke-width="3"/><circle cx="37" cy="37" r="10" stroke="#33b8a4" stroke-width="2.5"/><path d="M44 44l8 8" stroke="#33b8a4" stroke-width="2.5"/></svg>
    <h4>Searchable</h4><p>All data in the Lumora C-CDA is searchable, including previously unstructured data.</p>
  </div>
  <div class="benefit" style="left:640px">
    <svg width="80" height="80" viewBox="0 0 80 80" fill="none"><circle cx="40" cy="40" r="36" stroke="#2b2b38" stroke-width="3"/><path d="M40 76A36 36 0 0 1 6 52" stroke="#886aae" stroke-width="3"/><path d="M28 40h24M44 32l8 8-8 8" stroke="#b7a5cd" stroke-width="2.5"/></svg>
    <h4>Seamless Integration</h4><p>Designed for seamless integration into your current EHR workflow.</p>
  </div>
  <div class="benefit" style="left:900px">
    <svg width="80" height="80" viewBox="0 0 80 80" fill="none"><circle cx="40" cy="40" r="36" stroke="#2b2b38" stroke-width="3"/><path d="M4 40A36 36 0 0 1 40 4" stroke="#00a990" stroke-width="3"/><path d="M40 26v28M26 40h28M30 30l20 20M50 30L30 50" stroke="#ffffff" stroke-width="2"/></svg>
    <h4>Empower Physicians</h4><p>Provide physicians with a complete, summarized medical history, supporting the prevention of missed care.</p>
  </div>
</section>

<section class="blog">
  <h2 class="section-title" style="padding-top:20px">Latest Blog Posts</h2>
  <article class="card" style="left:120px">
    <div class="card__img" role="img" aria-label="Blog post photo of a clinical workspace"></div>
    <div class="card__box">There are many variations of dummy printing ...</div>
    <a class="btn btn--teal">Read More</a>
  </article>
  <article class="card" style="left:450px">
    <div class="card__img" role="img" aria-label="Blog post photo of a physician at a desk"></div>
    <div class="card__box">There are many variations of dummy printing ...</div>
    <a class="btn btn--purple">Read More</a>
  </article>
  <article class="card" style="left:780px">
    <div class="card__img" role="img" aria-label="Blog post photo of a hospital hallway"></div>
    <div class="card__box">There are many variations of dummy printing ...</div>
    <a class="btn btn--teal">Read More</a>
  </article>
</section>

<footer class="footer">
  <p>The Clarivio Lumora is a game-changing tool designed for healthcare sources to have all clinical records on hand, improving outcomes, reducing costs and giving care teams time back, significantly decreasing inefficiencies and administrative burden.</p>
  <p>Clarivio platform has been shaped by our partnerships with the leaders in value-based care to address their most complex challenges. We are experts in interoperability technology and are passionate about empowering healthcare organizations to achieve market-leading results.</p>
  <div class="footer__rule"></div>
  <p class="footer__copy">Copyright © CLARIVIO 2024. All Rights Reserved.</p>
  <div class="abs" style="right:60px;top:318px;width:22px;height:22px;border-radius:4px;background:var(--cyan)"></div>
</footer>

</body>
</html>
```